Print on top the name of the company: (Or Similar)
Larkmoor Cleaning & Disinfecting
Because your standards aren't standard.

We adhere to ALL NVB guidelines for both residential and commercial cleaning.

Infection Control is our ultimate goal.

Instructions:
Opening a residential and commercial cleaning and disinfecting company in south Florida.

Targeting high-end residential clients, commercial and healthcare facilities, specializing in Ambulatory Care Guidelines. With a concentration and expertise in targeting Covid 19 and other transmissible pathogens.

UMRE trained.
Owned and operated by a licensed BSN Registered Nurse specially ​trained in Infection Control Prevention with over 25 years experience. Over two decades in Ambulatory Surgery Center Administration, Director of Nursing and Infection Control Prevention ad Consulting.

Looking to create a business flier that emphasizes Cleaning & Disinfection
along with the standard expectation for residential and Commercial cleaning services
Updates

Need extra days to review

Target Market(s)

Residential & Commercial

Font styles to use
Decorative

Requirements
Must have
• A checklist for cleaning services

```html
<!DOCTYPE html>
<html lang="en">
<head>
<meta charset="utf-8">
<title>Larkmoor Cleaning &amp; Disinfecting</title>
<link href="https://fonts.googleapis.com/css2?family=Cabin:wght@700&family=Arimo:ital,wght@0,500;0,700;1,700&display=swap" rel="stylesheet">
<style>
  :root {
    --blue: #2b6fc1;
    --green: #6dbd2a;
    --green-dark: #4f9a14;
    --yellow: #f7ea2d;
    --white: #ffffff;
    --photo-a: #4f8fd6;
    --photo-b: #2f74c4;
  }
  html, body { margin: 0; padding: 0; overflow: hidden; }
  .flyer {
    position: relative;
    width: 927px; height: 1200px;
    background: var(--blue);
    overflow: hidden;
    font-family: "Arimo", Arial, sans-serif;
    color: var(--white);
  }
  .header-band { position: absolute; left: 0; top: 0; }
  .brand {
    position: absolute; left: 0; top: 58px; width: 927px;
    margin: 0; text-align: center;
    font-family: "Cabin", "Trebuchet MS", sans-serif;
    font-weight: 700; font-size: 64px; line-height: 78px;
    letter-spacing: 0.5px; text-transform: uppercase;
    text-shadow: 2px 3px 4px rgba(0,0,0,0.25);
  }
  .tagline {
    position: absolute; left: 0; top: 235px; width: 927px;
    margin: 0; text-align: center;
    font-style: italic; font-weight: 700; font-size: 25px;
  }
  .photo {
    position: absolute; left: 0; top: 365px; width: 470px; height: 835px;
    background: radial-gradient(ellipse at 45% 45%, var(--photo-a) 0%, var(--photo-b) 70%, var(--blue) 100%);
    border-radius: 0 200px 0 0;
  }
  .services { position: absolute; top: 398px; }
  .services.residential { left: 340px; }
  .services.commercial { left: 646px; }
  .services h2 {
    margin: 0 0 12px;
    font-family: "Cabin", "Trebuchet MS", sans-serif;
    font-size: 22px; font-weight: 700; letter-spacing: 0.5px;
    color: var(--yellow);
  }
  .services ul { list-style: none; margin: 0; padding: 0; }
  .services li { font-size: 21px; font-weight: 500; line-height: 23px; }
  .checklist {
    position: absolute; left: 645px; top: 662px; width: 260px;
    list-style: none; margin: 0; padding: 0;
  }
  .checklist li {
    position: relative; padding-left: 28px; margin-bottom: 11px;
    font-size: 18.5px; font-weight: 500; line-height: 21.5px;
  }
  .checklist svg { position: absolute; left: 0; top: 4px; }
  .call-now { position: absolute; left: 430px; top: 997px; }
  .phone {
    position: absolute; left: 597px; top: 1055px; margin: 0;
    font-family: "Cabin", "Trebuchet MS", sans-serif;
    font-weight: 700; font-size: 46px; letter-spacing: 1px;
    color: var(--yellow);
  }
</style>
</head>
<body>
<main class="flyer">
  <svg class="header-band" width="927" height="360" viewBox="0 0 927 360">
    <polygon points="0,0 927,0 927,280 463,358 0,280" fill="var(--green)"/>
  </svg>
  <h1 class="brand">Larkmoor Cleaning<br>&amp; Disinfecting</h1>
  <p class="tagline">Because your standards aren't standard.</p>

  <div class="photo" role="img" aria-label="Smiling cleaner in a blue apron and green gloves holding a bucket of cleaning supplies"></div>

  <section class="services residential">
    <h2>RESIDENTIAL</h2>
    <ul>
      <li>House cleaning</li>
      <li>Before &amp; after party</li>
      <li>Move-ins</li>
      <li>Move-outs</li>
      <li>Holiday cleaning</li>
      <li>Seasonal cleaning</li>
      <li>Carpet Cleaning</li>
      <li>Deodorizing &amp; sanitizing</li>
    </ul>
  </section>

  <section class="services commercial">
    <h2>COMMERCIAL</h2>
    <ul>
      <li>Janitorial</li>
      <li>Offices</li>
      <li>Floor maintenance</li>
      <li>Carpet cleaning</li>
      <li>Move-ins</li>
      <li>Construction clean-ups</li>
      <li>Estate clean-outs</li>
    </ul>
  </section>

  <ul class="checklist">
    <li><svg width="16" height="16" viewBox="0 0 16 16"><path d="M2 9 L6 13 L14 2" fill="none" stroke="var(--white)" stroke-width="2"/></svg>We adhere to ALL NVB guidelines for both residential and commercial cleaning.</li>
    <li><svg width="16" height="16" viewBox="0 0 16 16"><path d="M2 9 L6 13 L14 2" fill="none" stroke="var(--white)" stroke-width="2"/></svg>Infection Control is our ultimate goal.</li>
    <li><svg width="16" height="16" viewBox="0 0 16 16"><path d="M2 9 L6 13 L14 2" fill="none" stroke="var(--white)" stroke-width="2"/></svg>UMRE trained.</li>
    <li><svg width="16" height="16" viewBox="0 0 16 16"><path d="M2 9 L6 13 L14 2" fill="none" stroke="var(--white)" stroke-width="2"/></svg>Owned and operated by a licensed BSN Registered Nurse specially trained in Infection Control Prevention with over 25 years experience.</li>
  </ul>

  <svg class="call-now" width="150" height="150" viewBox="0 0 150 150">
    <defs>
      <radialGradient id="callGlow" cx="40%" cy="35%" r="70%">
        <stop offset="0" stop-color="#a6e04d"/>
        <stop offset="0.6" stop-color="var(--green)"/>
        <stop offset="1" stop-color="var(--green-dark)"/>
      </radialGradient>
    </defs>
    <circle cx="75" cy="75" r="72" fill="url(#callGlow)"/>
    <g transform="rotate(-15 75 75)" font-family="Arimo, Arial, sans-serif" font-weight="700" font-size="30" fill="var(--white)" text-anchor="middle">
      <text x="78" y="70">CALL</text>
      <text x="78" y="102">NOW</text>
    </g>
  </svg>
  <p class="phone">555-210-4478</p>
</main>
</body>
</html>
```